Back Pain

Need a flyer similar to the attached draft. This is to be handed out to prospective patients. Note that Sketch Hive has already designed the logo. If you need a copy please contact me

```html
<!DOCTYPE html>
<html lang="en">
<head>
<meta charset="utf-8">
<title>Tech Neck – Spine Ease Clinic</title>
<link href="https://fonts.googleapis.com/css2?family=Montserrat:ital,wght@0,400;0,500;0,600;0,700;1,400&family=Raleway:wght@400;500;600&display=swap" rel="stylesheet">
<style>
  :root {
    --green: #8cc63f;
    --blue: #1372bd;
    --panel: #4d4d4f;
    --soft: #f1f3f2;
    --ink: #231f20;
    --grey: #8c8c8c;
    --bar-grey: #a7a9ac;
    --photo-a: #2b3550;
    --photo-b: #c9d6d4;
  }
  * { margin: 0; padding: 0; box-sizing: border-box; }
  html, body { width: 849px; height: 1200px; overflow: hidden; background: #fff; }
  body { font-family: "Raleway", sans-serif; color: var(--ink); }
  .flyer { position: relative; width: 849px; height: 1200px; background: #fff; }

  .title {
    position: absolute; top: 48px; left: 0; width: 100%;
    text-align: center; font-family: "Montserrat", sans-serif;
    font-weight: 700; font-size: 80px; line-height: 90px; letter-spacing: -2px;
  }
  .title .tech { color: var(--green); }
  .title .neck { color: var(--blue); }

  .band { position: absolute; left: 0; width: 100%; height: 10px; }
  .band-top { top: 138px; background: linear-gradient(90deg, var(--blue), var(--green)); }
  .band-bottom { top: 777px; height: 11px; background: linear-gradient(90deg, var(--green), var(--blue)); }

  .photo {
    position: absolute; top: 148px; left: 0; width: 425px; height: 629px;
    background: linear-gradient(120deg, var(--photo-a) 0%, var(--photo-a) 40%, var(--photo-b) 100%);
  }
  .symptoms { position: absolute; left: 246px; top: 178px; list-style: none; }
  .symptoms li {
    display: inline-block; background: #fff; height: 33px; line-height: 34px;
    padding: 0 7px; font-size: 16px; font-weight: 500; color: var(--ink);
    position: absolute; left: 0; white-space: nowrap;
  }

  .stats { position: absolute; top: 148px; left: 425px; width: 424px; height: 629px; background: var(--panel); }
  .chart { position: absolute; top: 0; left: 0; }
  .device-time {
    position: absolute; top: 507px; left: 0; width: 100%; text-align: center; color: #fff;
  }
  .device-time .lead, .device-time .tail { font-size: 17px; font-weight: 400; line-height: 22px; }
  .device-time .hours {
    font-family: "Montserrat", sans-serif; font-weight: 700; font-size: 23px; line-height: 34px;
  }

  .message {
    position: absolute; top: 788px; left: 0; width: 100%; height: 145px; background: var(--soft);
    text-align: center; padding: 29px 40px 0; font-size: 23px; line-height: 32px; font-weight: 500;
  }
  .message .hl { color: var(--blue); font-weight: 600; }

  .clinic-mark { position: absolute; left: 37px; top: 976px; width: 360px; text-align: center; }
  .clinic-mark .dot { width: 128px; height: 128px; border-radius: 50%; background: var(--blue); margin: 0 auto 16px; }
  .clinic-mark .name {
    font-family: "Montserrat", sans-serif; font-weight: 600; color: var(--blue);
    font-size: 25px; line-height: 28px; letter-spacing: -0.5px;
  }
  .clinic-mark .sub {
    font-family: "Montserrat", sans-serif; font-weight: 600; color: var(--blue);
    font-size: 10.5px; letter-spacing: 3px; margin-top: 2px;
  }

  .contact { position: absolute; left: 447px; top: 972px; width: 330px; font-size: 13.5px; line-height: 16px; }
  .contact .doctor {
    font-family: "Montserrat", sans-serif; font-weight: 700; font-size: 19px; line-height: 24px;
    color: var(--blue); margin-bottom: 2px;
  }
  .contact .doctor .last { color: var(--green); }
  .contact p { margin: 0; }
  .contact .addr { line-height: 19px; }
  .contact strong { font-weight: 600; }
  .contact .offer {
    margin-top: 7px; width: 222px; border-top: 1.5px solid var(--grey); border-bottom: 1.5px solid var(--grey);
    padding: 3px 0 4px; font-family: "Montserrat", sans-serif; font-weight: 600; font-size: 13.5px; color: var(--grey);
    white-space: nowrap;
  }
  .contact .offer .off { color: var(--blue); font-weight: 700; }
  .contact .booking { margin-top: 14px; line-height: 20px; }
  .contact .booking em { font-style: italic; }

  .base-bar { position: absolute; left: 0; bottom: 0; width: 100%; height: 17px; background: var(--bar-grey); }
</style>
</head>
<body>
<main class="flyer">
  <h1 class="title"><span class="tech">TECH</span> <span class="neck">NECK</span></h1>
  <div class="band band-top"></div>

  <div class="photo" role="img" aria-label="Photo of a young businessman in a navy suit looking down at his smartphone"></div>
  <ul class="symptoms">
    <li style="top:0">HEADACHES</li>
    <li style="top:49px">NECK PAIN</li>
    <li style="top:98px">SHOULDER PAIN</li>
    <li style="top:147px">BACK PAIN</li>
    <li style="top:196px">ARM &amp; HANDPAIN</li>
    <li style="top:246px">SCIATICA</li>
  </ul>

  <section class="stats">
    <svg class="chart" width="424" height="460" viewBox="0 0 424 460" font-family="Raleway, sans-serif" fill="#fff">
      <text x="60" y="58" font-size="12" font-weight="500">As the Head Tilts Forward. More</text>
      <text x="60" y="76" font-size="12" font-weight="500">Force is placed on the Spine</text>
      <rect x="60" y="104" width="65" height="64" fill="#8a8a8c" role="img" aria-label="Small icon of a head tilting forward"/>
      <g>
        <rect x="60" y="260" width="41" height="46"/>
        <rect x="121" y="197" width="41" height="109"/>
        <rect x="183" y="140" width="40" height="166"/>
        <rect x="244" y="110" width="41" height="196"/>
        <rect x="306" y="66" width="40" height="240"/>
      </g>
      <g font-family="Montserrat, sans-serif" font-size="12" font-weight="500" text-anchor="middle">
        <text x="80" y="254">12</text>
        <text x="141" y="191">27</text>
        <text x="203" y="134">40</text>
        <text x="264" y="104">49</text>
        <text x="326" y="59">60</text>
        <text x="80" y="328">0˚</text>
        <text x="141" y="328">15˚</text>
        <text x="203" y="328">30˚</text>
        <text x="264" y="328">45˚</text>
        <text x="326" y="328">60˚</text>
      </g>
      <text x="212" y="355" font-size="13" font-weight="500" text-anchor="middle">Degrees of Forward Head Tilt</text>
      <text transform="translate(370 188) rotate(-90)" font-size="12" font-weight="500" text-anchor="middle">Pressure on Spine (LBS)</text>
      <circle cx="207" cy="447" r="34" fill="#fff"/>
    </svg>
    <svg class="chart" width="424" height="629" viewBox="0 0 424 629">
      <circle cx="207" cy="447" r="34" fill="#fff"/>
      <path d="M207 447 L207 413 A34 34 0 0 1 226.5 474.8 Z" fill="var(--blue)"/>
    </svg>
    <div class="device-time">
      <p class="lead">THE AVERAGE PERSON SPENDS</p>
      <p class="hours">8-11 HOURS PER DAY</p>
      <p class="tail">USING ELECTRONIC DEVICES</p>
    </div>
  </section>

  <div class="band band-bottom"></div>

  <section class="message">
    <p><span class="hl">Chiropractic Care</span> can help Correct and Prevent these problems by <span class="hl">Restoring</span> and <span class="hl">Maintaining Proper Alingment</span> of the <span class="hl">Neck</span></p>
  </section>

  <div class="clinic-mark">
    <div class="dot"></div>
    <p class="name">SPINE EASE CLINIC</p>
    <p class="sub">DR DAN MORROW - CHIROPRACTOR</p>
  </div>

  <section class="contact">
    <h2 class="doctor">DR DANIEL <span class="last">MORROW</span></h2>
    <p class="addr">Now in <strong>Harbourside</strong> at</p>
    <p class="addr">42 Market St- Arcade Suites</p>
    <p class="offer"><span class="off">50% OFF</span> INITIAL CONSULTATION</p>
    <div class="booking">
      <p><em>If you Book online at</em></p>
      <p><strong>www.spineeaseclinic.com.au</strong></p>
      <p>choose “<strong>Tech Neck</strong>” Option</p>
    </div>
  </section>

  <div class="base-bar"></div>
</main>
</body>
</html>
```